Vimcarra, Cosmetic skin care line

I am not looking to change my logo vimcarra on the label just want someone to design a different label I want it to be very classy as it is already just want something different. My product target classier people and people with higher income and for woman and men but mostly women. Looking to keep the label background black

Target Market(s)

Classier and higer income women/men mostly women

Industry/Entity Type

Cosmetics

• I don't really know

Colors

Designer to choose colors to be used in the design.

Requirements
Must have
• It must keep the same vimcarra logo and the same matte black background color
Nice to have
• I want a different layout and maybe different fonts for the label
Should not have

```html
<!DOCTYPE html>
<html lang="en">
<head>
<meta charset="utf-8">
<title>Vimcarra Eye Corrector Serum Label</title>
<link href="https://fonts.googleapis.com/css2?family=Montserrat:wght@400;500;600;700&family=Amatic+SC:wght@700&family=Tinos:wght@700&display=swap" rel="stylesheet">
<style>
  :root {
    --ink: #111113;
    --paper: #ffffff;
    --studio: #eeeeee;
    --divider: #1a1a1a;
  }
  * { box-sizing: border-box; margin: 0; padding: 0; }
  html, body { width: 1200px; height: 449px; overflow: hidden; }
  body { display: flex; font-family: "Montserrat", sans-serif; }

  .panel { height: 449px; display: flex; align-items: center; justify-content: center; }
  .panel--light { width: 269px; background: var(--paper); }
  .panel--dark { width: 270px; background: var(--ink); }
  .panel--studio { width: 336px; background: var(--studio); }
  .panel--studio-dark { width: 321px; background: var(--studio); }
  .divider { width: 4px; height: 449px; background: var(--divider); }

  .label {
    width: 141px; height: 150px;
    border: 2.4px solid var(--ink);
    display: flex; flex-direction: column; align-items: center;
    padding-top: 22px;
    color: var(--ink);
    white-space: nowrap;
    overflow: hidden;
  }
  .label--inverse { border-color: var(--paper); color: var(--paper); }

  .label__brand {
    font-family: "Montserrat", sans-serif;
    font-weight: 500;
    font-size: 19px;
    letter-spacing: 1px;
    line-height: 30px;
  }
  .label__tagline {
    font-family: "Amatic SC", sans-serif;
    font-weight: 700;
    font-size: 11px;
    letter-spacing: 1.5px;
    margin-top: 10px;
    line-height: 12px;
  }
  .label__product {
    font-weight: 500;
    font-size: 9.6px;
    letter-spacing: 2px;
    margin-top: 4px;
    line-height: 12px;
  }
  .label__type {
    font-family: "Tinos", serif;
    font-weight: 700;
    font-size: 15px;
    line-height: 16px;
  }
  .label__rule { width: 41px; height: 1px; background: currentColor; margin-top: 3px; }
  .label__feature {
    font-weight: 600;
    font-size: 9.4px;
    letter-spacing: 1.6px;
    margin-top: 4px;
    line-height: 11px;
  }
  .label__ingredient {
    font-weight: 600;
    font-size: 8px;
    line-height: 9px;
  }

  .wrap-band {
    width: 105px; height: 137px;
    margin-top: 112px;
    display: flex; align-items: center; justify-content: center;
  }
  .wrap-band--white { background: var(--paper); }
  .wrap-band--black { background: var(--ink); }
  .wrap-band .label { transform: scale(0.7); flex-shrink: 0; }
</style>
</head>
<body>
  <section class="panel panel--light">
    <div class="label">
      <p class="label__brand">VIMCARRA</p>
      <p class="label__tagline">FOR ALL</p>
      <p class="label__product">EYE CORRECTOR</p>
      <p class="label__type">Serum</p>
      <span class="label__rule"></span>
      <p class="label__feature">WITH TRIPLE</p>
      <p class="label__ingredient">PEPTIDES</p>
    </div>
  </section>

  <section class="panel panel--dark">
    <div class="label label--inverse">
      <p class="label__brand">VIMCARRA</p>
      <p class="label__tagline">FOR ALL</p>
      <p class="label__product">EYE CORRECTOR</p>
      <p class="label__type">Serum</p>
      <span class="label__rule"></span>
      <p class="label__feature">WITH TRIPLE</p>
      <p class="label__ingredient">PEPTIDES</p>
    </div>
  </section>

  <section class="panel panel--studio">
    <div class="wrap-band wrap-band--white">
      <div class="label">
        <p class="label__brand">VIMCARRA</p>
        <p class="label__tagline">FOR ALL</p>
        <p class="label__product">EYE CORRECTOR</p>
        <p class="label__type">Serum</p>
        <span class="label__rule"></span>
        <p class="label__feature">WITH TRIPLE</p>
        <p class="label__ingredient">PEPTIDES</p>
      </div>
    </div>
  </section>

  <div class="divider"></div>

  <section class="panel panel--studio-dark">
    <div class="wrap-band wrap-band--black">
      <div class="label label--inverse">
        <p class="label__brand">VIMCARRA</p>
        <p class="label__tagline">FOR ALL</p>
        <p class="label__product">EYE CORRECTOR</p>
        <p class="label__type">Serum</p>
        <span class="label__rule"></span>
        <p class="label__feature">WITH TRIPLE</p>
        <p class="label__ingredient">PEPTIDES</p>
      </div>
    </div>
  </section>
</body>
</html>
```